2 Redfern Pike Auto Care Banners

Looking to have two pull up banners designed - each 33.5 x 80

First banner- Scheduled Maintenance, Diagnostics, Inspections
Voted Top Pick Marbury 3 years in a row!

Second banner- Brakes, Tires, General Auto Service
Include the 3 TPM logos
2019, 2018, 2017

```html
<!DOCTYPE html>
<html lang="en">
<head>
<meta charset="utf-8">
<title>Redfern Pike Auto Care – Pull-up Banners</title>
<link href="https://fonts.googleapis.com/css2?family=Bebas+Neue&family=Roboto:wght@400;500&display=swap" rel="stylesheet">
<style>
  :root {
    --navy: #2b3358;
    --navy-deep: #1c2140;
    --gold: #c4b865;
    --stage: #a6a9ab;
    --white: #ffffff;
    --photo-blue: #3d4f7a;
    --photo-grey: #8a929c;
  }
  * { margin: 0; padding: 0; box-sizing: border-box; }
  html, body { width: 1162px; height: 1200px; overflow: hidden; background: var(--stage); }
  .canvas { position: relative; width: 1162px; height: 1200px; }

  .banner { position: absolute; width: 441px; height: 1051px; background: var(--white); overflow: hidden; }
  .banner--maintenance { left: 121px; top: 92px; }
  .banner--tires { left: 628px; top: 93px; }
  .banner__shapes { position: absolute; inset: 0; width: 441px; height: 1051px; }

  .brand-name {
    position: absolute; left: 0; width: 100%; text-align: center;
    font-family: 'Bebas Neue', sans-serif; font-weight: 400;
    color: var(--gold); font-size: 44px; line-height: 42px; letter-spacing: 1px;
  }
  .banner--maintenance .brand-name { top: 548px; }
  .banner--tires .brand-name { top: 40px; }

  .headline {
    position: absolute; left: 0; width: 100%; text-align: center;
    font-family: 'Bebas Neue', sans-serif; color: var(--navy);
    font-size: 27px; line-height: 28px; letter-spacing: 0.2px;
  }
  .banner--maintenance .headline { top: 667px; }
  .banner--tires .headline { top: 585px; }

  .service { position: absolute; display: flex; align-items: center; gap: 17px; }
  .service__icon {
    width: 36px; height: 36px; border: 1.5px solid var(--gold); border-radius: 5px;
    display: flex; align-items: center; justify-content: center; background: var(--white);
  }
  .service__icon svg { width: 24px; height: 24px; }
  .service__label {
    font-family: 'Bebas Neue', sans-serif; color: var(--navy);
    font-size: 24px; line-height: 24px; letter-spacing: 0.3px; padding-top: 3px;
  }

  .thumb {
    position: absolute; border: 1.5px solid var(--gold); border-radius: 4px;
  }
  .thumb--engine { background: linear-gradient(135deg, #2f3d5e, #7d8796 60%, #3a4358); }
  .thumb--laptop { background: linear-gradient(135deg, #c9ccd0, #6d7683 55%, #2e3650); }
  .thumb--hands { background: linear-gradient(135deg, #4a5a7d, #9aa2ab 50%, #2c3346); }
  .thumb--wheel { background: linear-gradient(135deg, #5b6371, #2b2f36 55%, #8b9099); }
  .thumb--impact { background: linear-gradient(135deg, #4d6d83, #6f9cad 50%, #2d3f56); }
  .thumb--rack { background: linear-gradient(90deg, #d9c9a8, #3c3a36 40%, #b5a88d 70%, #2e2c29); }

  .award { position: absolute; width: 86px; height: 40px; border-radius: 20px; background: #d6d8dc; }

  .contact { position: absolute; left: 0; top: 931px; width: 100%; text-align: center; }
  .contact__web { font-family: 'Roboto', sans-serif; font-weight: 500; font-size: 14px; color: var(--navy); line-height: 17px; }
  .contact__phone {
    margin: 3px auto 0; width: 183px; height: 23px; background: var(--navy); border-radius: 3px;
    display: flex; align-items: center; justify-content: center; gap: 8px;
    font-family: 'Bebas Neue', sans-serif; color: var(--white); font-size: 19px; letter-spacing: 0.8px; padding-top: 2px;
  }
  .contact__phone svg { width: 13px; height: 13px; margin-top: -2px; }
  .contact__address { margin-top: 5px; font-family: 'Roboto', sans-serif; font-weight: 500; font-size: 13.5px; color: var(--navy); line-height: 16px; }
</style>
</head>
<body>
<main class="canvas">

  <!-- Banner 1: maintenance -->
  <section class="banner banner--maintenance">
    <svg class="banner__shapes" viewBox="0 0 441 1051" aria-hidden="false">
      <defs>
        <linearGradient id="photoMechanic" x1="0" y1="0" x2="1" y2="1">
          <stop offset="0" stop-color="#2e3f73"/>
          <stop offset="0.5" stop-color="#5d6d8e"/>
          <stop offset="1" stop-color="#a9b1bb"/>
        </linearGradient>
      </defs>
      <rect width="441" height="560" fill="var(--navy)"/>
      <polygon points="300,0 441,0 441,118" fill="var(--navy-deep)"/>
      <polygon points="0,0 0,18 441,132 441,116" fill="var(--gold)"/>
      <g role="img" aria-label="Mechanic in blue overalls holding wrenches in front of a car engine in a workshop">
        <polygon points="0,18 441,132 441,515 0,416" fill="url(#photoMechanic)"/>
      </g>
      <polygon points="0,416 441,515 441,545 0,435" fill="var(--gold)"/>
      <polygon points="0,518 150,463 441,545 441,1051 0,1051" fill="var(--white)"/>
      <polygon points="0,989 175,1030 0,1051" fill="var(--gold)"/>
      <polygon points="0,1051 441,989 441,1051" fill="var(--navy)"/>
    </svg>

    <div class="brand-name">Redfern Pike<br>Auto Care</div>
    <h2 class="headline">Voted Top Pick Marbury 3 Years in a Row!</h2>

    <div class="service" style="left:38px; top:714px;">
      <span class="service__icon">
        <svg viewBox="0 0 24 24" fill="none" stroke="var(--navy)" stroke-width="1.6">
          <rect x="3" y="5" width="18" height="15" rx="1"/><line x1="3" y1="9" x2="21" y2="9"/>
          <line x1="7" y1="3" x2="7" y2="6"/><line x1="17" y1="3" x2="17" y2="6"/>
          <path d="M7 12h2M11 12h2M15 12h2M7 16h2M11 16h2M15 16h2"/>
        </svg>
      </span>
      <span class="service__label">Scheduled Maintenance</span>
    </div>
    <div class="service" style="left:39px; top:762px;">
      <span class="service__icon">
        <svg viewBox="0 0 24 24" fill="none" stroke="var(--navy)" stroke-width="1.6">
          <path d="M2 15v-3l2-4h8l2 4v3z"/><circle cx="5.5" cy="16" r="1.5"/><circle cx="11" cy="16" r="1.5"/>
          <circle cx="18" cy="14" r="4"/><path d="M16.2 14l1.3 1.3 2.3-2.5"/>
        </svg>
      </span>
      <span class="service__label">Diagnostics</span>
    </div>
    <div class="service" style="left:220px; top:765px;">
      <span class="service__icon">
        <svg viewBox="0 0 24 24" fill="none" stroke="var(--navy)" stroke-width="1.6">
          <rect x="3" y="4" width="18" height="13" rx="1"/><line x1="8" y1="20" x2="16" y2="20"/>
          <path d="M7 13v-2l1.5-2.5h7L17 11v2z" fill="var(--navy)"/>
        </svg>
      </span>
      <span class="service__label">Inspections</span>
    </div>

    <div class="thumb thumb--engine" style="left:29px; top:821px; width:116px; height:101px;" role="img" aria-label="Mechanic checking oil under an open car hood"></div>
    <div class="thumb thumb--laptop" style="left:153px; top:821px; width:117px; height:101px;" role="img" aria-label="Technician with laptop and clipboard running engine diagnostics"></div>
    <div class="thumb thumb--hands" style="left:280px; top:821px; width:116px; height:101px;" role="img" aria-label="Hands in gloves inspecting an engine bay"></div>

    <div class="contact">
      <p class="contact__web">www.redfernpikeauto.com</p>
      <p class="contact__phone">
        <svg viewBox="0 0 24 24" fill="var(--white)"><path d="M6.6 10.8a15 15 0 0 0 6.6 6.6l2.2-2.2c.3-.3.7-.4 1-.2 1.1.4 2.3.6 3.6.6.6 0 1 .4 1 1V20c0 .6-.4 1-1 1A17 17 0 0 1 3 4c0-.6.4-1 1-1h3.5c.6 0 1 .4 1 1 0 1.3.2 2.5.6 3.6.1.3 0 .7-.2 1z"/></svg>
        555-014-2290
      </p>
      <p class="contact__address">1820 Larkmoor Ln Marbury, VA 20999</p>
    </div>
  </section>

  <!-- Banner 2: tires -->
  <section class="banner banner--tires">
    <svg class="banner__shapes" viewBox="0 0 441 1051">
      <defs>
        <linearGradient id="photoTire" x1="0" y1="0" x2="1" y2="1">
          <stop offset="0" stop-color="#2c3a6b"/>
          <stop offset="0.55" stop-color="#3a3c42"/>
          <stop offset="1" stop-color="#c9ccd0"/>
        </linearGradient>
      </defs>
      <polygon points="0,130 0,213 199,170" fill="var(--navy)"/>
      <polygon points="0,213 441,127 441,140 0,225" fill="var(--gold)"/>
      <g role="img" aria-label="Mechanic kneeling to mount a tire onto a lifted car">
        <polygon points="0,225 441,140 441,446 0,532" fill="url(#photoTire)"/>
      </g>
      <polygon points="0,532 441,446 441,458 0,547" fill="var(--gold)"/>
      <polygon points="441,458 441,522 304,485" fill="var(--navy)"/>
      <polygon points="0,989 175,1030 0,1051" fill="var(--gold)"/>
      <polygon points="0,1051 441,989 441,1051" fill="var(--navy)"/>
    </svg>

    <div class="brand-name">Redfern Pike<br>Auto Care</div>
    <h2 class="headline">Tires and Auto Repair in Marbury, VA</h2>

    <div class="service" style="left:34px; top:633px;">
      <span class="service__icon">
        <svg viewBox="0 0 24 24" fill="none" stroke="var(--navy)" stroke-width="1.6">
          <path d="M4 18h12l-4-6 5-7 3 2-3 5"/><line x1="3" y1="21" x2="21" y2="21"/><path d="M4 12l8 6"/>
        </svg>
      </span>
      <span class="service__label">Brakes</span>
    </div>
    <div class="service" style="left:210px; top:633px;">
      <span class="service__icon">
        <svg viewBox="0 0 24 24" fill="none" stroke="var(--navy)" stroke-width="1.6">
          <path d="M2 18v-3l2-3h7l1 3v3z" fill="var(--navy)"/><circle cx="15" cy="9" r="5"/><line x1="18.5" y1="12.5" x2="22" y2="16"/>
        </svg>
      </span>
      <span class="service__label">General Service</span>
    </div>
    <div class="service" style="left:34px; top:679px;">
      <span class="service__icon">
        <svg viewBox="0 0 24 24" fill="none" stroke="var(--navy)" stroke-width="1.6">
          <circle cx="12" cy="12" r="9" fill="var(--navy)"/><circle cx="12" cy="12" r="4" stroke="var(--white)"/>
          <circle cx="12" cy="12" r="1" fill="var(--white)" stroke="none"/>
        </svg>
      </span>
      <span class="service__label">Tires</span>
    </div>
    <div class="service" style="left:210px; top:679px;">
      <span class="service__icon">
        <svg viewBox="0 0 24 24" fill="none" stroke="var(--navy)" stroke-width="1.8">
          <line x1="5" y1="19" x2="19" y2="5"/><line x1="5" y1="5" x2="19" y2="19"/>
          <circle cx="5" cy="5" r="2"/><circle cx="19" cy="5" r="2"/>
        </svg>
      </span>
      <span class="service__label">Much More</span>
    </div>

    <div class="thumb thumb--wheel" style="left:28px; top:737px; width:122px; height:107px;" role="img" aria-label="Technician removing a wheel beside an air hose"></div>
    <div class="thumb thumb--impact" style="left:158px; top:737px; width:124px; height:107px;" role="img" aria-label="Gloved hand using an impact wrench on an alloy wheel"></div>
    <div class="thumb thumb--rack" style="left:292px; top:737px; width:125px; height:107px;" role="img" aria-label="Stacked tires on a warehouse rack"></div>

    <div class="award" style="left:58px; top:869px;" role="img" aria-label="Top Pick Marbury 2017 award badge"></div>
    <div class="award" style="left:172px; top:869px;" role="img" aria-label="Top Pick Marbury 2018 award badge"></div>
    <div class="award" style="left:287px; top:869px;" role="img" aria-label="Top Pick Marbury 2019 award badge"></div>

    <div class="contact">
      <p class="contact__web">www.redfernpikeauto.com</p>
      <p class="contact__phone">
        <svg viewBox="0 0 24 24" fill="var(--white)"><path d="M6.6 10.8a15 15 0 0 0 6.6 6.6l2.2-2.2c.3-.3.7-.4 1-.2 1.1.4 2.3.6 3.6.6.6 0 1 .4 1 1V20c0 .6-.4 1-1 1A17 17 0 0 1 3 4c0-.6.4-1 1-1h3.5c.6 0 1 .4 1 1 0 1.3.2 2.5.6 3.6.1.3 0 .7-.2 1z"/></svg>
        555-014-2290
      </p>
      <p class="contact__address">1820 Larkmoor Ln Marbury, VA 20999</p>
    </div>
  </section>

</main>
</body>
</html>
```